M&A Advisory firm needs elegant and powerful letterhead

We need a powerful but elegant letterhead to engage with the international financial industry.

Target Market(s)

New York and International Financial Industry

Industry/Entity Type

Finance

Font styles to use
Other font styles liked:
• Poppins

Requirements
Must have
• 482 W 71st Street 14th Floor New York, NY 10157 O: +1 (212) 555 0147 F: +1 (212) 555 0182

```html
<!DOCTYPE html>
<html lang="en">
<head>
<meta charset="utf-8">
<title>Halvern Letterhead</title>
<link href="https://fonts.googleapis.com/css2?family=Poppins:wght@400;500;600&family=Arimo:wght@400&display=swap" rel="stylesheet">
<style>
  :root {
    --canvas-bg: #ededed;
    --paper: #e6e6e6;
    --brand-blue: #0c4a86;
    --rule-grey: #717175;
    --text-dark: #4a4a4d;
    --text-light: #e8eef6;
    --faint-mark: #d6d6d6;
  }
  * { margin: 0; padding: 0; box-sizing: border-box; }
  html, body {
    width: 1200px; height: 1024px; overflow: hidden;
    background: var(--canvas-bg);
  }
  .letterhead {
    position: absolute; left: 260px; top: 32px;
    width: 679px; height: 960px;
    background: var(--paper);
    overflow: hidden;
    box-shadow: 0 2px 10px rgba(0,0,0,0.12);
  }
  .header-band { position: absolute; left: 0; top: 0; width: 679px; height: 150px; }
  .brand {
    position: absolute; left: 48px; top: 68px;
    display: flex; align-items: center; gap: 12px;
  }
  .brand-dot { width: 30px; height: 30px; border-radius: 50%; background: var(--brand-blue); }
  .brand-name {
    font-family: "Poppins", sans-serif; font-weight: 400;
    font-size: 40px; letter-spacing: 1px; color: var(--brand-blue); line-height: 1;
  }
  .contact {
    position: absolute; left: 475px; top: 38px;
    font-family: "Arimo", Arial, sans-serif; font-size: 11.5px; line-height: 13.5px;
    color: var(--text-light);
  }
  .contact-line { display: flex; align-items: center; gap: 4px; }
  .contact-line svg { width: 9px; height: 9px; }
  .contact-address { margin-top: 4px; }
  .salutation {
    position: absolute; left: 61px; top: 293px;
    font-family: "Poppins", sans-serif; font-weight: 500; font-size: 16px;
    color: var(--text-dark);
  }
  .body-copy {
    position: absolute; left: 60px; top: 339px; width: 562px;
    font-family: "Arimo", Arial, sans-serif; font-size: 12.2px; line-height: 14px;
    color: var(--text-dark);
  }
  .body-copy p { margin-bottom: 12px; }
  .closing {
    position: absolute; left: 61px; top: 628px;
    font-family: "Poppins", sans-serif; font-weight: 600; font-size: 9px;
    color: var(--text-dark);
  }
  .signature {
    position: absolute; left: 61px; top: 667px; width: 112px; height: 34px;
    background: linear-gradient(90deg, #d9d9d9, #cfcfcf);
    border-radius: 4px;
  }
  .faint-mark {
    position: absolute; left: 468px; top: 744px;
    width: 100px; height: 100px; border-radius: 50%;
    background: var(--faint-mark);
  }
</style>
</head>
<body>
  <main class="letterhead">
    <svg class="header-band" viewBox="0 0 679 150" aria-hidden="true">
      <rect x="0" y="0" width="679" height="22" fill="var(--brand-blue)"/>
      <path fill="var(--brand-blue)" d="M420,0 H679 V128 H470 Q440,128 440,100 V22 Q440,0 420,0 Z"/>
      <rect x="0" y="140" width="679" height="3" fill="var(--rule-grey)"/>
    </svg>

    <div class="brand">
      <span class="brand-dot"></span>
      <span class="brand-name">Halvern</span>
    </div>

    <div class="contact">
      <div class="contact-line">
        <svg viewBox="0 0 10 10"><path fill="none" stroke="currentColor" stroke-width="1.2" d="M2,1 L4,3 L3,4.2 C3.6,5.5 4.5,6.4 5.8,7 L7,6 L9,8 L7.8,9.2 C4.5,8.8 1.2,5.5 0.8,2.2 Z"/></svg>
        <span>+1 (212) 555 0147</span>
      </div>
      <div class="contact-line">
        <svg viewBox="0 0 10 10"><rect x="2.5" y="1" width="5" height="3" fill="none" stroke="currentColor" stroke-width="1"/><rect x="1" y="4" width="8" height="5" fill="none" stroke="currentColor" stroke-width="1"/></svg>
        <span>+1 (212) 555 0182</span>
      </div>
      <div class="contact-address">
        482 W 71st Street<br>
        14th Floor New York, NY 10157
      </div>
    </div>

    <h1 class="salutation">Dear Mr. Harlow,</h1>

    <section class="body-copy">
      <p>Lorem ipsum dolor sit amet, consectetuer adipiscing elit, sed diam nonmmy nibh euismod tincidunt ut laor eet dolore magna aliquam erat volutpat. Ut wisi enim ad minim veniam, quis nostrud exerci tationmcorper suscipit lobortis nisl ut aliquip ex ea commodo consequat. Duis autem vel eum iriure dolor in hendrerit in vulputate velit esse molestie consequat, vel illum dolore eu feugiat</p>
      <p>Rorem ipsum dolor sit amet, consectetuer adipiscing elit, sed diam nonmmy nibh euismod tincidunt ut laor eet dolore magna aliquam erat volutpat. Ut wisi enim ad minim veniam, quis nostrud exerci tationmcorper suscipit lobortis nisl ut aliquip ex ea commodo consequat. Duis autem vel eum iriure dolor in hendrerit in vulputate velit esse molest</p>
      <p>Dorem ipsum dolor sit amet, consectetuer adipiscing elit, sed diam nonmmy nibh euismod tincidunt ut laor eet dolore magna aliquam erat volutpat. Ut wisi enim ad minim veniam, quis nostrud exerci tationmcorper suscipit lobortis nisl ut aliquip ex ea commodo consequat. Duis autem vel eum iriure dolor in hendrerit in suscipit lobortis nisl ut aliquip ex ea commodo consequat. Duis autem vel eum iriure dolor in hendrerit in vulputate velit esse molestie consequat, vel illum</p>
      <p>Sorem ipsum dolor sit amet, consectetuer adipiscing elit, sed diam nonmmy nibh euismod tincidunt ut laor eet dolore magna aliquam erat volutpat. Ut wisi enim ad minim veniam, quis nostrud exerci tationmcorper suscipit lobortis nisl ut aliquip ex ea commodo consequat. Duis autem vel eum iriure dolor in</p>
    </section>

    <p class="closing">Sincerely,</p>
    <div class="signature" role="img" aria-label="Handwritten signature of the sender"></div>

    <div class="faint-mark" aria-hidden="true"></div>
  </main>
</body>
</html>
```